Android application design for shared calendar app

I need an Android app design for shared calendar, It should have a business look&feel,flat material design. Main part of UI are big clock-like wheels which represent free time and busy time. Busy is red ,free is green. App should have business look & feel but it should be still usable for non business users.

app can be seen here,please try it before starting design
https://apps.quorvexia.com/store/apps/details?id=com.tivralo&hl=en

here is a video: https://vorbelclips.com/hR3kPq9LmZ2

Target Market(s)

busy business professionals

Industry/Entity Type

Business

Font styles to use
Sans Serif

Requirements
Must have
• 1) project must have big clock-like circles in which free time is marked in green, busy time in red. so those colors must be green and red but you can use which shades.
• 2) project must have one 16:9 ratio image which has text : click here to load picture which describes your event. and under that text several pictures - business meeting, phone call,some people playing sports,some people in pub. I have attached how it currently look - don't use it, thats just a example :)
• 3) must have default placeholder for user image. I also attached how it currently looks
• 4) buttons and dialogs must be rounded - see how it looks in the app
• 5) events must have semi transparent overlay - see how it looks in the app. font for location and event name can be changed
• 6) App must use eurofurencebold regular for title in action bar., that can't be changed. App must use existing logo (green overlapping clocks)
Nice to have
• a loading page with progress bar should have some interesting picture (city for example)

```html
<!DOCTYPE html>
<html lang="en">
<head>
<meta charset="utf-8">
<title>Tivralo – Tomorrow</title>
<link href="https://fonts.googleapis.com/css2?family=Roboto:wght@400;500&display=swap" rel="stylesheet">
<style>
  :root {
    --status-bar: #1a1a1a;
    --app-bar: #212121;
    --tab-divider: #333333;
    --tab-idle: #8a8a8a;
    --on-dark: #ffffff;
    --surface: #f5f5f5;
    --busy: #ef6276;
    --free: #4caf50;
    --hub-text: #6a6a6a;
    --avatar-bg: #ececec;
    --avatar-fg: #c8c8c8;
    --name-text: #666666;
    --meta-text: #a8a8a8;
    --row-divider: #e0e0e0;
  }
  html, body { margin: 0; padding: 0; }
  body {
    width: 675px; height: 1200px; overflow: hidden;
    background: var(--surface);
    font-family: "Roboto", sans-serif;
  }
  .screen {
    position: relative; width: 720px; height: 1280px;
    transform: scale(0.9375); transform-origin: 0 0;
    background: var(--surface); overflow: hidden;
  }
  .status-bar {
    position: absolute; left: 0; top: 0; width: 720px; height: 48px;
    background: var(--status-bar);
  }
  .status-bar .clock {
    position: absolute; right: 16px; top: 8px;
    color: var(--on-dark); font-size: 26px; line-height: 32px;
  }
  .status-bar svg { position: absolute; top: 10px; }
  .app-bar {
    position: absolute; left: 0; top: 48px; width: 720px; height: 134px;
    background: var(--app-bar);
  }
  .brand-dot {
    position: absolute; left: 37px; top: 26px; width: 84px; height: 84px;
    border-radius: 50%; background: var(--free);
  }
  .app-title {
    position: absolute; left: 142px; top: 44px; margin: 0;
    color: var(--on-dark); font-size: 38px; font-weight: 500; line-height: 48px;
  }
  .overflow-menu { position: absolute; right: 30px; top: 48px; }
  .tabs {
    position: absolute; left: 0; top: 182px; width: 720px; height: 81px;
    background: var(--app-bar); border-top: 1px solid var(--tab-divider);
    display: flex; box-sizing: border-box;
    box-shadow: 0 2px 4px rgba(0,0,0,0.18);
  }
  .tab {
    position: relative; flex: 1; text-align: center;
    font-size: 24px; font-weight: 500; letter-spacing: 1px;
    line-height: 80px; color: var(--tab-idle);
  }
  .tab.is-active { color: var(--on-dark); }
  .tab.is-active::after {
    content: ""; position: absolute; left: 0; right: 0; bottom: 0;
    height: 5px; background: var(--on-dark);
  }
  .wheel { position: absolute; }
  .wheel .hour { fill: var(--on-dark); font-size: 25px; font-family: "Roboto", sans-serif; }
  .wheel .hub-label { fill: var(--hub-text); font-family: "Roboto", sans-serif; }
  .day-wheels .wheel { top: 305px; width: 346px; height: 346px; }
  .contact {
    position: absolute; left: 0; width: 720px; height: 270px;
  }
  .contact .wheel { top: 42px; width: 180px; height: 180px; }
  .avatar { position: absolute; left: 35px; top: 42px; }
  .contact-name {
    position: absolute; left: 36px; top: 228px;
    color: var(--name-text); font-size: 24px; font-weight: 500;
  }
  .last-seen {
    position: absolute; right: 36px; top: 230px;
    color: var(--meta-text); font-size: 21px;
  }
  .contact + .contact { border-top: 1px solid var(--row-divider); }
</style>
</head>
<body>
<div class="screen">

  <div class="status-bar">
    <svg style="left:514px" width="36" height="28" viewBox="0 0 36 28" aria-hidden="true">
      <path d="M0 6 Q18 -6 36 6 L18 28 Z" fill="#fff"/>
    </svg>
    <svg style="left:556px" width="28" height="28" viewBox="0 0 28 28" aria-hidden="true">
      <path d="M28 0 L28 28 L0 28 Z" fill="#fff"/>
    </svg>
    <svg style="left:600px" width="18" height="28" viewBox="0 0 18 28" aria-hidden="true">
      <rect x="5" y="0" width="8" height="3" fill="#fff"/>
      <rect x="0" y="3" width="18" height="25" rx="1" fill="#fff"/>
    </svg>
    <span class="clock">12:30</span>
  </div>

  <header class="app-bar">
    <span class="brand-dot"></span>
    <h1 class="app-title">Tivralo</h1>
    <svg class="overflow-menu" width="12" height="40" viewBox="0 0 12 40" aria-label="More options">
      <circle cx="6" cy="5" r="5" fill="#fff"/>
      <circle cx="6" cy="20" r="5" fill="#fff"/>
      <circle cx="6" cy="35" r="5" fill="#fff"/>
    </svg>
  </header>

  <nav class="tabs">
    <div class="tab">TODAY</div>
    <div class="tab is-active">TOMORROW</div>
    <div class="tab">MONDAY</div>
  </nav>

  <section class="day-wheels">
    <!-- Morning -->
    <svg class="wheel" style="left:2px" viewBox="-173 -173 346 346" aria-label="Morning availability">
      <circle r="173" fill="var(--busy)"/>
      <g stroke="rgba(255,255,255,0.3)" stroke-width="1.2">
        <line x1="0" y1="0" x2="0" y2="-173"/><line x1="0" y1="0" x2="86.5" y2="-149.8"/>
        <line x1="0" y1="0" x2="149.8" y2="-86.5"/><line x1="0" y1="0" x2="173" y2="0"/>
        <line x1="0" y1="0" x2="149.8" y2="86.5"/><line x1="0" y1="0" x2="86.5" y2="149.8"/>
        <line x1="0" y1="0" x2="0" y2="173"/><line x1="0" y1="0" x2="-86.5" y2="149.8"/>
        <line x1="0" y1="0" x2="-149.8" y2="86.5"/><line x1="0" y1="0" x2="-173" y2="0"/>
        <line x1="0" y1="0" x2="-149.8" y2="-86.5"/><line x1="0" y1="0" x2="-86.5" y2="-149.8"/>
      </g>
      <circle r="80" fill="rgba(255,255,255,0.5)"/>
      <circle r="71" fill="#fff"/>
      <g class="hour" text-anchor="middle" dominant-baseline="central">
        <text x="30.5" y="-114">00</text><text x="83.4" y="-83.4">01</text>
        <text x="114" y="-30.5">02</text><text x="114" y="30.5">03</text>
        <text x="83.4" y="83.4">04</text><text x="30.5" y="114">05</text>
        <text x="-30.5" y="114">06</text><text x="-83.4" y="83.4">07</text>
        <text x="-114" y="30.5">08</text><text x="-114" y="-30.5">09</text>
        <text x="-83.4" y="-83.4">10</text><text x="-30.5" y="-114">11</text>
      </g>
      <text class="hub-label" font-size="36" text-anchor="middle" dominant-baseline="central">AM</text>
    </svg>

    <!-- Afternoon -->
    <svg class="wheel" style="left:373px" viewBox="-173 -173 346 346" aria-label="Afternoon availability">
      <circle r="173" fill="var(--free)"/>
      <path d="M0 0 L0 -173 A173 173 0 0 1 149.8 86.5 Z" fill="var(--busy)"/>
      <path d="M0 0 L86.5 149.8 A173 173 0 0 1 0 173 Z" fill="var(--busy)"/>
      <g stroke="rgba(255,255,255,0.3)" stroke-width="1.2">
        <line x1="0" y1="0" x2="0" y2="-173"/><line x1="0" y1="0" x2="86.5" y2="-149.8"/>
        <line x1="0" y1="0" x2="149.8" y2="-86.5"/><line x1="0" y1="0" x2="173" y2="0"/>
        <line x1="0" y1="0" x2="149.8" y2="86.5"/><line x1="0" y1="0" x2="86.5" y2="149.8"/>
        <line x1="0" y1="0" x2="0" y2="173"/><line x1="0" y1="0" x2="-86.5" y2="149.8"/>
        <line x1="0" y1="0" x2="-149.8" y2="86.5"/><line x1="0" y1="0" x2="-173" y2="0"/>
        <line x1="0" y1="0" x2="-149.8" y2="-86.5"/><line x1="0" y1="0" x2="-86.5" y2="-149.8"/>
      </g>
      <circle r="80" fill="rgba(255,255,255,0.5)"/>
      <circle r="71" fill="#fff"/>
      <g class="hour" text-anchor="middle" dominant-baseline="central">
        <text x="30.5" y="-114" font-style="italic">12</text><text x="83.4" y="-83.4">13</text>
        <text x="114" y="-30.5">14</text><text x="114" y="30.5" font-style="italic">15</text>
        <text x="83.4" y="83.4">16</text><text x="30.5" y="114">17</text>
        <text x="-30.5" y="114">18</text><text x="-83.4" y="83.4">19</text>
        <text x="-114" y="30.5">20</text><text x="-114" y="-30.5">21</text>
        <text x="-83.4" y="-83.4">22</text><text x="-30.5" y="-114">23</text>
      </g>
      <text class="hub-label" font-size="36" text-anchor="middle" dominant-baseline="central">PM</text>
    </svg>
  </section>

  <!-- Contact 1 -->
  <article class="contact" style="top:795px">
    <svg class="avatar" width="182" height="182" viewBox="0 0 182 182" aria-label="Default user picture">
      <circle cx="91" cy="91" r="91" fill="var(--avatar-bg)"/>
      <circle cx="91" cy="64" r="27" fill="var(--avatar-fg)"/>
      <path d="M41 146 A50 48 0 0 1 141 146 Z" fill="var(--avatar-fg)"/>
    </svg>
    <svg class="wheel" style="left:271px" viewBox="-173 -173 346 346" aria-label="Morning availability">
      <circle r="173" fill="var(--busy)"/>
      <path d="M0 0 L-173 0 A173 173 0 0 1 0 -173 Z" fill="var(--free)"/>
      <g stroke="rgba(255,255,255,0.3)" stroke-width="2">
        <line x1="0" y1="0" x2="0" y2="-173"/><line x1="0" y1="0" x2="86.5" y2="-149.8"/>
        <line x1="0" y1="0" x2="149.8" y2="-86.5"/><line x1="0" y1="0" x2="173" y2="0"/>
        <line x1="0" y1="0" x2="149.8" y2="86.5"/><line x1="0" y1="0" x2="86.5" y2="149.8"/>
        <line x1="0" y1="0" x2="0" y2="173"/><line x1="0" y1="0" x2="-86.5" y2="149.8"/>
        <line x1="0" y1="0" x2="-149.8" y2="86.5"/><line x1="0" y1="0" x2="-173" y2="0"/>
        <line x1="0" y1="0" x2="-149.8" y2="-86.5"/><line x1="0" y1="0" x2="-86.5" y2="-149.8"/>
      </g>
      <circle r="80" fill="rgba(255,255,255,0.5)"/>
      <circle r="71" fill="#fff"/>
      <text class="hub-label" font-size="34" text-anchor="middle" dominant-baseline="central">AM</text>
    </svg>
    <svg class="wheel" style="left:505px" viewBox="-173 -173 346 346" aria-label="Afternoon availability">
      <circle r="173" fill="var(--free)"/>
      <g stroke="rgba(255,255,255,0.3)" stroke-width="2">
        <line x1="0" y1="0" x2="0" y2="-173"/><line x1="0" y1="0" x2="86.5" y2="-149.8"/>
        <line x1="0" y1="0" x2="149.8" y2="-86.5"/><line x1="0" y1="0" x2="173" y2="0"/>
        <line x1="0" y1="0" x2="149.8" y2="86.5"/><line x1="0" y1="0" x2="86.5" y2="149.8"/>
        <line x1="0" y1="0" x2="0" y2="173"/><line x1="0" y1="0" x2="-86.5" y2="149.8"/>
        <line x1="0" y1="0" x2="-149.8" y2="86.5"/><line x1="0" y1="0" x2="-173" y2="0"/>
        <line x1="0" y1="0" x2="-149.8" y2="-86.5"/><line x1="0" y1="0" x2="-86.5" y2="-149.8"/>
      </g>
      <circle r="80" fill="rgba(255,255,255,0.5)"/>
      <circle r="71" fill="#fff"/>
      <text class="hub-label" font-size="34" text-anchor="middle" dominant-baseline="central">PM</text>
    </svg>
    <span class="contact-name">Name</span>
    <span class="last-seen">Yesterday</span>
  </article>

  <!-- Contact 2 -->
  <article class="contact" style="top:1065px">
    <svg class="avatar" width="182" height="182" viewBox="0 0 182 182" aria-label="Default user picture">
      <circle cx="91" cy="91" r="91" fill="var(--avatar-bg)"/>
      <circle cx="91" cy="64" r="27" fill="var(--avatar-fg)"/>
      <path d="M41 146 A50 48 0 0 1 141 146 Z" fill="var(--avatar-fg)"/>
    </svg>
    <svg class="wheel" style="left:271px" viewBox="-173 -173 346 346" aria-label="Morning availability">
      <circle r="173" fill="var(--busy)"/>
      <g stroke="rgba(255,255,255,0.3)" stroke-width="2">
        <line x1="0" y1="0" x2="0" y2="-173"/><line x1="0" y1="0" x2="86.5" y2="-149.8"/>
        <line x1="0" y1="0" x2="149.8" y2="-86.5"/><line x1="0" y1="0" x2="173" y2="0"/>
        <line x1="0" y1="0" x2="149.8" y2="86.5"/><line x1="0" y1="0" x2="86.5" y2="149.8"/>
        <line x1="0" y1="0" x2="0" y2="173"/><line x1="0" y1="0" x2="-86.5" y2="149.8"/>
        <line x1="0" y1="0" x2="-149.8" y2="86.5"/><line x1="0" y1="0" x2="-173" y2="0"/>
        <line x1="0" y1="0" x2="-149.8" y2="-86.5"/><line x1="0" y1="0" x2="-86.5" y2="-149.8"/>
      </g>
      <circle r="80" fill="rgba(255,255,255,0.5)"/>
      <circle r="71" fill="#fff"/>
      <text class="hub-label" font-size="34" text-anchor="middle" dominant-baseline="central">AM</text>
    </svg>
    <svg class="wheel" style="left:505px" viewBox="-173 -173 346 346" aria-label="Afternoon availability">
      <circle r="173" fill="var(--free)"/>
      <path d="M0 0 L149.8 86.5 A173 173 0 0 1 0 173 Z" fill="var(--busy)"/>
      <g stroke="rgba(255,255,255,0.3)" stroke-width="2">
        <line x1="0" y1="0" x2="0" y2="-173"/><line x1="0" y1="0" x2="86.5" y2="-149.8"/>
        <line x1="0" y1="0" x2="149.8" y2="-86.5"/><line x1="0" y1="0" x2="173" y2="0"/>
        <line x1="0" y1="0" x2="149.8" y2="86.5"/><line x1="0" y1="0" x2="86.5" y2="149.8"/>
        <line x1="0" y1="0" x2="0" y2="173"/><line x1="0" y1="0" x2="-86.5" y2="149.8"/>
        <line x1="0" y1="0" x2="-149.8" y2="86.5"/><line x1="0" y1="0" x2="-173" y2="0"/>
        <line x1="0" y1="0" x2="-149.8" y2="-86.5"/><line x1="0" y1="0" x2="-86.5" y2="-149.8"/>
      </g>
      <circle r="80" fill="rgba(255,255,255,0.5)"/>
      <circle r="71" fill="#fff"/>
      <text class="hub-label" font-size="34" text-anchor="middle" dominant-baseline="central">PM</text>
    </svg>
  </article>

</div>
</body>
</html>
```